Need a new logo/business card for a cafe

I need a new logo and business card for a café. The café is called "Ladle", and we have a reputation for making a high quality cup of espresso coffee. I would like the business card design to reflect this "high quality". Our baristas craft our customers coffee with care to achieve this result. I would like to see designs that include a warm latte brown color. The card will be single sided to allow the rear to be used as a loyalty card which means the design will need to include space for our business address, phone number, and facebook page details. The uploaded logo is already in use on the café front window, and if it can be incorporated or used that would be great, but I am open to completely new designs as well. Thank you.
Updates
Thank you to all for the submissions. There's quite a few I like now, the hardest part will be choosing! I've set up a poll for added feedback from my own contacts and will wait on results from that.
Hello, more great designs coming in, thank you very much. There's quite a few that I really like, so my biggest challenge is going to be choosing one. Thanks again for your time, and I'll get onto the hard task of making that choice. Marcia
Industry/Entity Type
Cafe
Look and feel
Each slider illustrates characteristics of the customer's brand and the style your logo design should communicate.

```html
<!DOCTYPE html>
<html lang="en">
<head>
<meta charset="UTF-8">
<title>Ladle — Business Card</title>
<link rel="stylesheet" href="https://fonts.googleapis.com/css2?family=Marcellus&display=swap">
<style>
  :root {
    --card-black: #000000;
    --latte-brown: #6e3817;
    --cream-text: #c6a493;
    --motif-glow: rgba(58, 34, 20, 0.55);
    --motif-fade: rgba(58, 34, 20, 0);
  }
  * { margin: 0; padding: 0; box-sizing: border-box; }
  html, body {
    width: 1200px;
    height: 720px;
    overflow: hidden;
    background: var(--card-black);
  }
  .business-card {
    position: relative;
    width: 1200px;
    height: 720px;
    overflow: hidden;
    background: var(--card-black);
    font-family: "Marcellus", serif;
  }
  .cup-motif {
    position: absolute;
    left: 400px;
    top: 96px;
    width: 410px;
    height: 530px;
    background:
      radial-gradient(ellipse 50% 28% at 58% 76%, var(--motif-glow), var(--motif-fade) 100%),
      radial-gradient(ellipse 14% 36% at 45% 34%, var(--motif-glow), var(--motif-fade) 100%);
  }
  .brand-name {
    position: absolute;
    left: 104px;
    top: 100px;
    font-size: 160px;
    line-height: 1;
    font-weight: 400;
    color: var(--latte-brown);
    letter-spacing: 2px;
  }
  .contact-list {
    position: absolute;
    left: 115px;
    top: 368px;
    list-style: none;
  }
  .contact-item {
    font-size: 42px;
    line-height: 80px;
    color: var(--cream-text);
    letter-spacing: 0.5px;
    white-space: nowrap;
  }
</style>
</head>
<body>
  <main class="business-card">
    <div class="cup-motif" role="img" aria-label="Faint steaming espresso cup decoration"></div>
    <h1 class="brand-name">Ladle</h1>
    <ul class="contact-list">
      <li class="contact-item">Address: Your Company Address</li>
      <li class="contact-item">Contact Number: Your Contact Details</li>
      <li class="contact-item">Page Details: Your Page Details</li>
    </ul>
  </main>
</body>
</html>
```